Pediatric Dental Practice needs a postcard for direct mail advertising

We are looking for a creative and professional double-sided postcard design for a direct mail marketing campaign. Our goal is to attract new families to our pediatric dental practice by conveying a sense of warmth, modern care, and clinical excellence. The design should feel "boutique" and high-end yet remain fun and approachable for parents and children.

```html
<!DOCTYPE html>
<html lang="en">
<head>
<meta charset="utf-8">
<title>Maple Grove Pediatric Dentistry – Postcard</title>
<link href="https://fonts.googleapis.com/css2?family=Lora:wght@500;600&family=Nunito+Sans:wght@400;600;700&display=swap" rel="stylesheet">
<style>
  :root {
    --backdrop: #0a4a52;
    --paper: #f8f6f2;
    --green: #5a9a55;
    --green-dark: #4f8c4b;
    --green-soft: #a7c29a;
    --green-pale: #c6d8bb;
    --mint: #e6efe0;
    --ink: #33363d;
    --rule: #c9d6c3;
  }
  * { box-sizing: border-box; margin: 0; padding: 0; }
  html, body { width: 1200px; height: 873px; overflow: hidden; }
  body { background: var(--backdrop); position: relative; font-family: "Nunito Sans", sans-serif; color: var(--ink); }

  .card { position: absolute; top: 76px; width: 506px; height: 720px; background: var(--paper); overflow: hidden; }
  .card--front { left: 68px; }
  .card--back { left: 635px; }

  /* Front */
  .brand { position: absolute; top: 56px; left: 0; width: 100%; text-align: center; }
  .brand__name { font-family: "Nunito Sans", sans-serif; font-weight: 600; font-size: 28px; color: var(--ink); letter-spacing: 0.5px; display: inline-flex; align-items: center; gap: 8px; }
  .brand__dot { width: 14px; height: 14px; border-radius: 50%; background: var(--green); display: inline-block; }
  .brand__sub { font-size: 9.5px; letter-spacing: 3.2px; font-weight: 600; margin-top: 2px; color: var(--ink); }

  .headline { position: absolute; top: 170px; left: 104px; font-family: "Lora", serif; font-weight: 600; font-size: 76px; line-height: 73px; letter-spacing: -1px; }
  .headline .hl-green { color: var(--green); display: block; }
  .headline .hl-ink { color: var(--ink); display: block; }

  .divider { position: absolute; display: flex; align-items: center; gap: 12px; }
  .divider__line { height: 1px; background: var(--rule); flex: 1; }
  .divider--front { top: 396px; left: 98px; width: 316px; }

  .tagline { position: absolute; top: 426px; left: 0; width: 100%; text-align: center; color: var(--green); font-size: 13.5px; font-weight: 600; letter-spacing: 1.2px; line-height: 21px; }

  .pill { position: absolute; top: 487px; left: 95px; width: 318px; height: 37px; border-radius: 19px; background: var(--green); color: #fff; display: flex; align-items: center; justify-content: center; gap: 10px; font-size: 13px; font-weight: 600; letter-spacing: 1.4px; }

  .waves { position: absolute; left: 0; bottom: 0; width: 506px; height: 200px; }
  .sprig { position: absolute; left: 4px; top: 500px; width: 80px; height: 180px; border-radius: 40px; background: linear-gradient(180deg, rgba(168,196,150,0.55), rgba(110,160,95,0.6)); }
  .sprig--top { left: 344px; top: 258px; width: 62px; height: 34px; border-radius: 20px; background: linear-gradient(90deg, rgba(168,196,150,0.5), rgba(140,180,120,0.6)); }

  /* Back */
  .back-title { position: absolute; top: 50px; left: 30px; font-family: "Lora", serif; font-weight: 500; font-size: 29px; line-height: 35px; }
  .back-title .t-green { color: var(--green); display: block; }
  .back-title .t-ink { color: var(--ink); }
  .heart-inline { display: inline-block; vertical-align: middle; margin-left: 4px; }
  .divider--back { top: 135px; left: 30px; width: 144px; }

  .audience { position: absolute; top: 158px; left: 30px; color: var(--green); font-size: 12px; font-weight: 600; letter-spacing: 1px; line-height: 18px; }

  .services { position: absolute; top: 212px; left: 12px; width: 216px; display: grid; grid-template-columns: repeat(3, 72px); row-gap: 10px; }
  .service { text-align: center; font-size: 10px; line-height: 14px; color: var(--ink); }
  .service__icon { width: 44px; height: 44px; border-radius: 50%; background: var(--mint); margin: 0 auto 7px; }

  .offer { position: absolute; top: 427px; left: 18px; width: 211px; height: 126px; background: var(--green); border-radius: 8px; color: #fff; text-align: center; }
  .offer__frame { position: absolute; inset: 5px; border: 1.2px dashed rgba(255,255,255,0.75); border-radius: 5px; }
  .offer__notch { position: absolute; top: -9px; left: 93px; width: 25px; height: 25px; border-radius: 50%; background: var(--paper); display: flex; align-items: center; justify-content: center; }
  .offer__amount { margin-top: 16px; font-family: "Lora", serif; font-weight: 600; font-size: 44px; line-height: 48px; }
  .offer__amount small { font-size: 29px; }
  .offer__line { font-size: 12.5px; font-weight: 600; letter-spacing: 0.3px; margin-top: 2px; }
  .offer__note { font-size: 10px; letter-spacing: 0.6px; margin-top: 10px; }

  .contact { position: absolute; top: 585px; left: 22px; list-style: none; font-size: 12.5px; line-height: 17px; }
  .contact li { display: flex; gap: 12px; margin-bottom: 8px; align-items: flex-start; }
  .contact svg { flex: none; margin-top: 2px; }

  .back-rule { position: absolute; left: 250px; top: 39px; width: 1px; height: 658px; background: var(--green-soft); }
  .stamp { position: absolute; left: 398px; top: 35px; width: 76px; height: 102px; border: 1px solid var(--ink); display: flex; align-items: center; justify-content: center; text-align: center; font-size: 12px; line-height: 20px; letter-spacing: 0.4px; }
  .address-line { position: absolute; left: 284px; width: 183px; height: 1px; background: var(--ink); opacity: 0.75; }
</style>
</head>
<body>

<section class="card card--front" aria-label="Postcard front">
  <div class="brand">
    <div class="brand__name"><span class="brand__dot"></span>maple grove</div>
    <div class="brand__sub">PEDIATRIC DENTISTRY</div>
  </div>

  <h1 class="headline">
    <span class="hl-green">Healthy</span>
    <span class="hl-green">smiles</span>
    <span class="hl-ink">grow here.</span>
  </h1>
  <div class="sprig sprig--top" role="img" aria-label="Small leaf sprig decoration"></div>

  <div class="divider divider--front">
    <span class="divider__line"></span>
    <svg width="18" height="16" viewBox="0 0 24 22"><path d="M12 21 2.5 11.5A5.5 5.5 0 0 1 12 4a5.5 5.5 0 0 1 9.5 7.5Z" fill="var(--green)"/></svg>
    <span class="divider__line"></span>
  </div>

  <p class="tagline">GENTLE CARE. MODERN TECHNOLOGY.<br>MADE FOR KIDS.</p>

  <div class="pill">
    <svg width="18" height="16" viewBox="0 0 24 22"><path d="M12 21 2.5 11.5A5.5 5.5 0 0 1 12 4a5.5 5.5 0 0 1 9.5 7.5Z" fill="#fff"/></svg>
    NOW WELCOMING NEW FAMILIES
  </div>

  <svg class="waves" viewBox="0 0 506 200" preserveAspectRatio="none" aria-hidden="true">
    <path d="M0 120 C90 70 170 90 250 130 C330 165 410 60 506 5 L506 200 L0 200Z" fill="var(--green-pale)"/>
    <path d="M0 150 C100 95 190 120 270 155 C350 185 420 100 506 55 L506 200 L0 200Z" fill="var(--green-soft)" opacity="0.85"/>
  </svg>
  <div class="sprig" role="img" aria-label="Leafy branch decoration"></div>
</section>

<section class="card card--back" aria-label="Postcard back">
  <h2 class="back-title">
    <span class="t-green">Big care for</span>
    <span class="t-ink">little smiles.</span><svg class="heart-inline" width="16" height="14" viewBox="0 0 24 22"><path d="M12 21 2.5 11.5A5.5 5.5 0 0 1 12 4a5.5 5.5 0 0 1 9.5 7.5Z" fill="var(--green)"/></svg>
  </h2>

  <div class="divider divider--back">
    <span class="divider__line"></span>
    <svg width="13" height="12" viewBox="0 0 24 22"><path d="M12 21 2.5 11.5A5.5 5.5 0 0 1 12 4a5.5 5.5 0 0 1 9.5 7.5Z" fill="var(--green)"/></svg>
    <span class="divider__line"></span>
  </div>

  <p class="audience">PEDIATRIC DENTISTRY<br>FOR AGES 0 TO TEEN</p>

  <div class="services">
    <div class="service"><div class="service__icon" role="img" aria-label="Preventive care icon"></div>Preventive<br>Care</div>
    <div class="service"><div class="service__icon" role="img" aria-label="Gentle care icon"></div>Gentle &amp;<br>Comforting</div>
    <div class="service"><div class="service__icon" role="img" aria-label="Restorative dentistry icon"></div>Restorative<br>Dentistry</div>
    <div class="service"><div class="service__icon" role="img" aria-label="Scheduling icon"></div>Convenient<br>Scheduling</div>
    <div class="service"><div class="service__icon" role="img" aria-label="Calm environment icon"></div>Calm<br>Environment</div>
    <div class="service"><div class="service__icon" role="img" aria-label="Orthodontic evaluation icon"></div>Orthodontic<br>Evaluations</div>
  </div>

  <div class="offer">
    <div class="offer__frame"></div>
    <div class="offer__notch"><svg width="13" height="12" viewBox="0 0 24 22"><path d="M12 21 2.5 11.5A5.5 5.5 0 0 1 12 4a5.5 5.5 0 0 1 9.5 7.5Z" fill="var(--green)"/></svg></div>
    <div class="offer__amount">$50 <small>OFF</small></div>
    <div class="offer__line">YOUR CHILD'S FIRST VISIT!</div>
    <div class="offer__note">MENTION THIS CARD.</div>
  </div>

  <ul class="contact">
    <li><svg width="13" height="15" viewBox="0 0 24 28"><path d="M12 27S3 17 3 10a9 9 0 0 1 18 0c0 7-9 17-9 17Z" fill="var(--green)"/><circle cx="12" cy="10" r="3.3" fill="var(--paper)"/></svg><span>48 Birch Lane, Suite 200<br>Fairview, SC 29000</span></li>
    <li><svg width="13" height="13" viewBox="0 0 24 24"><path d="M6.6 10.8a15 15 0 0 0 6.6 6.6l2.2-2.2a1 1 0 0 1 1-.25 11 11 0 0 0 3.6.57 1 1 0 0 1 1 1V20a1 1 0 0 1-1 1A17 17 0 0 1 3 4a1 1 0 0 1 1-1h3.5a1 1 0 0 1 1 1 11 11 0 0 0 .57 3.6 1 1 0 0 1-.25 1Z" fill="var(--green)"/></svg><span>(555) 010-2468</span></li>
    <li><svg width="13" height="13" viewBox="0 0 24 24"><circle cx="12" cy="12" r="10" fill="none" stroke="var(--green)" stroke-width="2.4"/><path d="M2 12h20M12 2c3 3 3 17 0 20M12 2c-3 3-3 17 0 20" fill="none" stroke="var(--green)" stroke-width="2"/></svg><span>maplegrovedental.com</span></li>
    <li><svg width="13" height="13" viewBox="0 0 24 24"><circle cx="12" cy="12" r="11" fill="var(--green)"/></svg><span>@maplegrovedental</span></li>
  </ul>

  <div class="back-rule"></div>
  <div class="stamp">PLACE<br>STAMP<br>HERE</div>
  <div class="address-line" style="top:318px"></div>
  <div class="address-line" style="top:359px"></div>
  <div class="address-line" style="top:399px"></div>
  <div class="address-line" style="top:440px"></div>
</section>

</body>
</html>
```